Postcard Design

I need a postcard to use as a mailer and handout piece to get a new vacation rental management company off the ground. This will be sent to rental property owners in Solvane on 30a in Florida.

A google image search of "Solvane 30A" will provide plenty of images for look and feel of the project. A quick google of "coastal modern design" will provide some feel for interiors and a color palette using the beachy but subtle colors typical to that decor.

Solvane is a 130 unit condominium complex in a very active beach rental market. The tone of the community is upscale family vacations...it is NOT a party destination. Beach and family time are what most people are here for.

Logo file uploaded here.

If good design comes in quickly I may zero in on one quickly to tweak it and get things moving.

Target audience is property owners who we hope to bring in as rental owners. The audience is not rental guests. Try to sell to property owners who you want to trust us with their investments.

We offer a full lineup of services including top-notch housekeeping, maintenance, marketing, and guest services.

We want to build relationships with our property owners.

We are a small team focused on only Solvane properties.

Designers...please feel free to suggest any wording or tag lines that you think sell this idea. Your creativity with the copy is as valuable as your visual creativity.

Some copy scraps & messaging to play with:

Tailored exclusively to Solvane and its owners

Boutique Rental Management

Full service maintenance and housekeeping

Solvane's reputation is our reputation

Thank you all.

I just updated he brief to provide some added guidance. Thanks!

Boutique

```html
<!DOCTYPE html>
<html lang="en">
<head>
<meta charset="utf-8">
<title>Solvane Postcard – Front and Back</title>
<link rel="stylesheet" href="https://fonts.googleapis.com/css2?family=Source+Sans+3:wght@300;400&display=swap">
<style>
  :root {
    --page-bg: #ffffff;
    --sand: #ddd0ac;
    --teal: #4d9fb0;
    --teal-light: #d6eef2;
    --cocoa: #3d2a21;
    --ink: #3b2a22;
    --cream: #faf2e6;
    --stamp: #a9cfcc;
    --rule: #c9bcaa;
    --hairline: #bdb3a6;
    --white: #ffffff;
  }
  * { box-sizing: border-box; margin: 0; padding: 0; }
  html, body {
    width: 1200px; height: 1000px; overflow: hidden;
    background: var(--page-bg);
    font-family: "Source Sans 3", "Helvetica Neue", Arial, sans-serif;
  }
  .postcard {
    position: absolute; top: 291px;
    width: 537px; height: 417px; overflow: hidden;
  }
  .postcard--front { left: 52px; }
  .postcard--back { left: 611px; background: var(--cream); border: 1px solid var(--hairline); }

  .tile-strip {
    position: absolute; left: 0; width: 100%; height: 12px;
    background: linear-gradient(90deg, #8fc3d6, #d9cfb1 20%, #5a9ec0 40%, #bfe0ea 60%, #d9cfb1 80%, #6fa9c9);
  }
  .tile-strip--top { top: 0; }
  .tile-strip--bottom { bottom: 0; }

  .photo-row { position: absolute; top: 12px; left: 0; width: 100%; height: 135px; display: flex; }
  .photo { height: 100%; }
  .photo--boardwalk { width: 132px; background: linear-gradient(180deg, #9cc6e6, #c9b89a 60%, #7a6a55); }
  .photo--building { width: 135px; background: linear-gradient(180deg, #7fb0e0, #e6d08e 45%, #5f8a4a); }
  .photo--beach { width: 133px; background: linear-gradient(180deg, #a8d4d8, #e8ecec 55%, #f4f2ea); }
  .photo--pool { width: 137px; background: linear-gradient(180deg, #5c8f5e, #8ecfe0 45%, #d9d4c8); }

  .brand-band {
    position: absolute; top: 147px; left: 0; width: 100%; height: 95px;
    background: var(--sand); text-align: center;
  }
  .brand-name {
    display: inline-block; margin-top: 26px;
    font-size: 44px; font-weight: 300; color: var(--ink); letter-spacing: 1px;
    line-height: 1; padding-bottom: 6px; border-bottom: 1.5px solid var(--ink);
  }
  .headline-band {
    position: absolute; top: 242px; left: 0; width: 100%; height: 30px;
    background: var(--teal); color: var(--teal-light);
    font-size: 19px; font-weight: 300; letter-spacing: 0.6px;
    text-align: center; line-height: 30px;
  }
  .pitch {
    position: absolute; top: 272px; left: 0; width: 100%; height: 132px;
    background: var(--cocoa); color: var(--white);
    text-align: center; font-size: 11.5px; line-height: 15.5px; padding-top: 12px;
  }
  .pitch__contact { margin-top: 10px; font-size: 12px; }

  .back-photo {
    position: absolute; left: 48px; top: 25px; width: 166px; height: 203px;
    background: linear-gradient(180deg, #8fb6de, #d9c27c 35%, #7a9a5c 60%, #7fcde0);
  }
  .back-brand {
    position: absolute; left: 40px; top: 254px; width: 182px; text-align: center;
  }
  .back-brand .brand-name { margin-top: 0; font-size: 36px; padding-bottom: 4px; }
  .tagline {
    position: absolute; left: 40px; top: 314px; width: 182px;
    text-align: center; font-size: 12.5px; line-height: 13px; color: var(--ink);
  }
  .divider {
    position: absolute; left: 259px; top: 28px; width: 1px; height: 312px; background: var(--ink);
  }
  .stamp-box {
    position: absolute; left: 420px; top: 25px; width: 85px; height: 100px;
    background: var(--stamp); padding: 7px;
  }
  .stamp-box__frame { width: 100%; height: 100%; border: 1.5px solid var(--white); }
  .address-line {
    position: absolute; left: 305px; width: 200px; height: 2px; background: var(--rule);
  }
</style>
</head>
<body>
  <section class="postcard postcard--front" aria-label="Postcard front">
    <div class="tile-strip tile-strip--top" role="img" aria-label="Mosaic tile border in blues and sand"></div>
    <div class="photo-row">
      <div class="photo photo--boardwalk" role="img" aria-label="Photo of a wooden boardwalk leading to the beach"></div>
      <div class="photo photo--building" role="img" aria-label="Photo of the condominium building with palm trees"></div>
      <div class="photo photo--beach" role="img" aria-label="Photo of white sand beach with blue umbrellas"></div>
      <div class="photo photo--pool" role="img" aria-label="Photo of the hot tub and pool area"></div>
    </div>
    <div class="brand-band"><span class="brand-name">Solvane</span></div>
    <div class="headline-band">HAS A BUSINESS PROPOSAL JUST FOR YOU</div>
    <div class="pitch">
      <p>We are a small team of Solvane's Condo experts.</p>
      <p>Find your investment opportunity here at the beautiful Solvane by Coastline.</p>
      <p>Let our real estate professionals personally assist you.</p>
      <p>We offer state of the art marketing, complete guest services,</p>
      <p>top notch housekeeping and all year round maintenance.</p>
      <p class="pitch__contact">Contact us at: Toll Free: (866) 555-0147</p>
    </div>
    <div class="tile-strip tile-strip--bottom" role="img" aria-label="Mosaic tile border in blues and sand"></div>
  </section>

  <section class="postcard postcard--back" aria-label="Postcard back">
    <div class="back-photo" role="img" aria-label="Photo of the condominium and pool"></div>
    <div class="back-brand"><span class="brand-name">Solvane</span></div>
    <p class="tagline">knows how to improve<br>your incomes.</p>
    <div class="divider"></div>
    <div class="stamp-box"><div class="stamp-box__frame"></div></div>
    <div class="address-line" style="top:190px"></div>
    <div class="address-line" style="top:229px"></div>
    <div class="address-line" style="top:266px"></div>
    <div class="address-line" style="top:304px"></div>
    <div class="address-line" style="top:342px"></div>
    <div class="tile-strip tile-strip--bottom" role="img" aria-label="Mosaic tile border in blues and sand"></div>
  </section>
</body>
</html>
```